Website For Custom Home Builder

-Very elegant and simple design as I am a high end custom home builder.
-I build homes $2 million to $10 million range so the website needs to reflect the level of home that I build.
-Attached are photos of homes I have built to use as well as my logo.
-I need final design to be in layered format so my local guy can edit if he needs to.

3 Page Design
1. HomePage:
-logo, some photos,
-“Building beautiful custom homes in Indianapolis for over 20 years”
2. AboutPage:
-Wade Holloran has been building stunning custom homes in the Indianpolis area for over 20 years. As a small boutique building company we only build a handful of homes a year in order to offer our clients the personal attention that their homes deserve. It's this attention to detail that makes our client experience and final product something special and unique.
- family photo
3. ContactPage:
-office photo
-317-552-7190
-wade@whcrafted.com
-415 North Fernmill Rd, Suite 308, Carmel IN 46033

Target Market(s)

Very high end clients looking to build $2 million to $10 million homes.

Industry/Entity Type

Residential high end custom home builder/construction

Coding

Coded - Design and coding required

Number of Pages Required

3 page

Requirements
Must have
• Very simple and elegant design that represents the high end homes that I build.
Nice to have
Should not have
• Should NOT have a lot of clutter or be a very busy page from a design perspective.

```html
<!DOCTYPE html>
<html lang="en">
<head>
<meta charset="utf-8">
<title>Wade Holloran Custom Homes</title>
<link href="https://fonts.googleapis.com/css2?family=Montserrat:wght@300;400;500;600;700;800&display=swap" rel="stylesheet">
<style>
:root{
  --brown:#b05a1c;
  --brown-dark:#8a4514;
  --brown-deep:#5e3212;
  --band:#a8561b;
  --ink:#222222;
  --text:#3a3a3a;
  --blush:#fdeee3;
  --charcoal:#2e2e2e;
  --white:#ffffff;
  --light:#efefef;
}
*{margin:0;padding:0;box-sizing:border-box}
html,body{width:1200px;height:4471px;overflow:hidden}
body{position:relative;background:var(--white);font-family:'Montserrat',sans-serif;color:var(--text)}
.photo{position:absolute}
.btn{position:absolute;display:flex;align-items:center;justify-content:center;gap:12px;font-weight:700;font-size:13px;letter-spacing:.5px;text-transform:uppercase}
.btn svg{flex:none}
.rule{width:84px;height:4px;background:var(--brown);margin:12px 0 22px}
h2.section-title{font-size:31px;font-weight:700;color:var(--ink);letter-spacing:.5px}

/* header */
.site-header{position:absolute;left:0;top:0;width:1200px;height:92px;background:var(--white)}
.brand{position:absolute;left:104px;top:22px;display:flex;align-items:center;gap:14px;color:#4a4a4a}
.brand-mark{width:44px;height:44px;border:3px solid var(--brown)}
.brand-name{font-size:26px;font-weight:400;line-height:1;letter-spacing:-.5px}
.brand-sub{font-size:11px;font-weight:400;letter-spacing:6.4px;margin-top:5px}
.main-nav{position:absolute;top:36px;left:537px;display:flex;gap:40px;font-size:16px;color:#333}
.call{position:absolute;left:966px;top:26px;display:flex;gap:12px;align-items:center}
.call small{display:block;font-size:14px;color:#333}
.call b{display:block;font-size:11px;font-weight:500;color:#333;margin-top:3px}

/* hero */
.hero{position:absolute;left:0;top:92px;width:1200px;height:640px;overflow:hidden}
.hero-photo{left:0;top:0;width:1200px;height:640px;
  background:
    radial-gradient(ellipse 260px 120px at 560px 420px,rgba(255,176,80,.55),rgba(255,176,80,0)),
    radial-gradient(ellipse 180px 90px at 860px 380px,rgba(255,170,70,.4),rgba(255,170,70,0)),
    radial-gradient(ellipse 220px 60px at 1080px 540px,rgba(70,120,190,.75),rgba(70,120,190,0)),
    radial-gradient(ellipse 360px 80px at 160px 560px,rgba(70,100,50,.8),rgba(70,100,50,0)),
    linear-gradient(180deg,#c98d54 0%,#d59a5c 10%,#8a5a36 24%,#4b3224 42%,#3a281d 62%,#4a3a28 80%,#39432b 100%)}
.hero-box{position:absolute;left:146px;top:122px;width:908px;height:278px;background:rgba(120,108,96,.55)}
.hero-title{position:absolute;left:0;top:170px;width:1200px;text-align:center;color:var(--white);font-size:44px;line-height:55px;font-weight:300;letter-spacing:1px}
.hero-title b{font-weight:700}
.hero .btn{left:521px;top:365px;width:158px;height:42px;background:var(--brown);color:var(--white)}
.hero-shape{position:absolute;left:0;top:0}

/* custom homes */
.custom{position:absolute;left:0;top:804px;width:1200px;height:313px}
.custom-intro{position:absolute;left:104px;top:58px;width:300px}
.custom-intro p{font-size:14px;line-height:22px;color:#333}
.arrows{display:flex;gap:16px;margin-top:18px}
.home-card{position:absolute;top:0;width:261px;height:310px;overflow:hidden}
.home-card .label{position:absolute;left:0;bottom:0;width:100%;height:56px;padding:0 14px;display:flex;align-items:center;justify-content:space-between;color:var(--white);font-weight:700;font-size:20px;background:linear-gradient(0deg,rgba(0,0,0,.6),rgba(0,0,0,0))}

/* about */
.about{position:absolute;left:0;top:1195px;width:1200px;height:560px;background:linear-gradient(180deg,#a9581c,#a4531a 60%,#9c4f18)}
.about-photo{left:163px;top:68px;width:346px;height:400px;
  background:
    radial-gradient(ellipse 120px 150px at 170px 260px,rgba(180,60,50,.5),rgba(180,60,50,0)),
    radial-gradient(ellipse 160px 80px at 170px 380px,rgba(90,120,60,.7),rgba(90,120,60,0)),
    linear-gradient(180deg,#b9cde0 0%,#d9d3c8 25%,#cfc6b6 50%,#a79c8a 75%,#6e7a4e 100%);
  clip-path:polygon(0 14%,50% 0,100% 14%,100% 100%,0 100%)}
.about-text{position:absolute;left:643px;top:106px;width:455px;color:var(--white)}
.about-text .section-title{color:var(--white)}
.about-text .rule{background:var(--white)}
.about-lead{font-size:14px;font-weight:700;line-height:24px;margin-bottom:14px}
.about-body{font-size:13.5px;line-height:24px}
.about .btn{position:relative;margin-top:24px;width:160px;height:44px;border:1px solid var(--white);color:var(--white)}

/* builder */
.builder-box{position:absolute;left:104px;top:1954px;width:792px;height:441px;background:var(--blush)}
.builder-text{position:absolute;left:60px;top:76px;width:480px}
.builder-text h2{font-size:33px;line-height:42px;font-weight:700;color:var(--ink)}
.builder-text p{font-size:14px;line-height:22px;color:#444;margin-top:12px}
.builder-text p + p{margin-top:8px}
.builder-box .btn{left:60px;top:328px;width:158px;height:42px;background:var(--brown);color:var(--white)}
.builder-photo{left:686px;top:1836px;width:408px;height:456px;border:4px solid var(--white);box-shadow:0 0 8px rgba(0,0,0,.2);
  background:
    radial-gradient(ellipse 70px 40px at 300px 300px,rgba(255,150,60,.6),rgba(255,150,60,0)),
    radial-gradient(ellipse 110px 140px at 90px 220px,rgba(120,150,90,.55),rgba(120,150,90,0)),
    linear-gradient(180deg,#6b4a30 0%,#8a6446 8%,#e4e0da 18%,#eeebe6 55%,#d9d5cf 72%,#b8946e 88%,#9a7654 100%)}

/* testimonial */
.quote-band{position:absolute;left:0;top:2479px;width:1200px;height:325px;background:linear-gradient(180deg,#6b3a16,#8a4a1b 50%,#6b3a16)}
.quote-text{position:absolute;left:170px;top:85px;width:860px;text-align:center;color:var(--white);font-size:17.5px;line-height:27px;font-weight:400}
.quote-author{position:absolute;left:0;top:210px;width:1200px;text-align:center;color:var(--white);font-weight:700;font-size:27px}

/* projects */
.projects-title{position:absolute;left:0;top:2872px;width:1200px;text-align:center}
.projects-title .rule{margin:10px auto 0;width:84px}

/* contact */
.contact{position:absolute;left:0;top:3644px;width:1200px;height:560px;background:var(--light);overflow:hidden}
.office-photo{left:0;top:0;width:600px;height:560px;
  background:
    radial-gradient(ellipse 130px 180px at 300px 200px,rgba(150,185,120,.95),rgba(150,185,120,0)),
    radial-gradient(ellipse 220px 90px at 360px 470px,rgba(120,60,30,.85),rgba(120,60,30,0)),
    linear-gradient(90deg,#2b2b2b 0%,#3a3a3a 18%,#8fa57c 40%,#c9d2bd 55%,#dcdcd8 75%,#efefef 100%)}
.contact-text{position:absolute;left:643px;top:82px;width:410px}
.contact-text p.intro{font-size:11.5px;line-height:18px;color:#444}
.contact-item{display:flex;gap:22px;margin-top:26px;align-items:flex-start}
.contact-item .dot{width:40px;height:40px;border-radius:50%;background:var(--brown-deep);display:flex;align-items:center;justify-content:center;flex:none}
.contact-item h4{font-size:15px;font-weight:600;color:#222}
.contact-item span{display:block;font-size:11px;line-height:18px;color:#555;margin-top:4px}

/* footer */
.site-footer{position:absolute;left:0;top:4100px;width:1200px;height:371px}
.footer-shape{position:absolute;left:0;top:0}
.footer-brand{position:absolute;left:0;top:120px;width:1200px;text-align:center;color:var(--white)}
.footer-brand .sq{width:34px;height:34px;border:3px solid var(--white);margin:0 auto 14px}
.footer-brand .name{font-size:34px;font-weight:400;letter-spacing:-.5px;line-height:1}
.footer-brand .sub{font-size:14px;font-weight:400;letter-spacing:10px;margin-top:6px}
.footer-nav{position:absolute;left:0;top:250px;width:1200px;display:flex;justify-content:center;gap:36px;color:var(--white);font-size:15px}
.footer-line{position:absolute;left:104px;top:292px;width:992px;height:1px;background:#555}
.copyright{position:absolute;left:104px;top:334px;font-size:11px;color:var(--white)}
.social{position:absolute;left:985px;top:324px;display:flex;gap:14px}
.social span{width:26px;height:26px;border-radius:50%;background:var(--white)}
</style>
</head>
<body>

<header class="site-header">
  <div class="brand">
    <div class="brand-mark"></div>
    <div>
      <div class="brand-name">WADE HOLLORAN</div>
      <div class="brand-sub">CUSTOM HOMES</div>
    </div>
  </div>
  <nav class="main-nav"><span>Home</span><span>About Us</span><span>Project</span><span>Contact Us</span></nav>
  <div class="call">
    <svg width="32" height="32" viewBox="0 0 24 24"><path d="M6.6 10.8c1.4 2.8 3.8 5.1 6.6 6.6l2.2-2.2c.3-.3.7-.4 1-.2 1.1.4 2.3.6 3.6.6.6 0 1 .4 1 1V20c0 .6-.4 1-1 1C10.6 21 3 13.4 3 4c0-.6.4-1 1-1h3.5c.6 0 1 .4 1 1 0 1.3.2 2.5.6 3.6.1.3 0 .7-.2 1z" fill="none" stroke="#222" stroke-width="1.6"/></svg>
    <div><small>Call Us :</small><b>317-552-7190</b></div>
  </div>
</header>

<section class="hero">
  <div class="photo hero-photo" role="img" aria-label="Custom stone and timber home at dusk with lit patio and pool"></div>
  <div class="hero-box"></div>
  <h1 class="hero-title">BUILDING <b>BEAUTIFUL</b><br><b>CUSTOM HOMES</b> IN INDIANAPOLIS<br>FOR <b>OVER 20 YEARS</b></h1>
  <div class="btn">Get Started
    <svg width="16" height="10" viewBox="0 0 16 10"><path d="M0 5h14M10 1l4 4-4 4" stroke="#fff" stroke-width="1.6" fill="none"/></svg>
  </div>
  <svg class="hero-shape" width="1200" height="640" viewBox="0 0 1200 640">
    <defs>
      <linearGradient id="heroBand" x1="0" x2="1" y1="0" y2="0">
        <stop offset="0" stop-color="#5e3212"/><stop offset=".5" stop-color="#b05a1c"/><stop offset="1" stop-color="#5e3212"/>
      </linearGradient>
    </defs>
    <polygon points="0,599 600,495 1200,599 1200,640 0,640" fill="#ffffff"/>
    <polygon points="0,599 600,495 1200,599 1200,614 600,511 0,614" fill="url(#heroBand)"/>
    <polygon points="300,560 600,612 900,560 930,570 600,630 270,570" fill="url(#heroBand)"/>
  </svg>
</section>

<section class="custom">
  <div class="custom-intro">
    <h2 class="section-title">CUSTOM HOMES</h2>
    <div class="rule"></div>
    <p>Lorem ipsum dolor sit amet, consectetur adipiscing elit, sed do eiusmod tempor incididunt ut labore et dolore magna aliqua.</p>
    <div class="arrows">
      <svg width="20" height="12" viewBox="0 0 20 12"><path d="M20 6H2M6 1L1 6l5 5" stroke="#222" stroke-width="2" fill="none"/></svg>
      <svg width="20" height="12" viewBox="0 0 20 12"><path d="M0 6h18M14 1l5 5-5 5" stroke="#222" stroke-width="2" fill="none"/></svg>
    </div>
  </div>
  <div class="home-card" style="left:478px">
    <div class="photo" style="inset:0;background:radial-gradient(ellipse 90px 60px at 160px 210px,rgba(255,170,80,.55),rgba(255,170,80,0)),linear-gradient(180deg,#d89a5e 0%,#a9744a 18%,#5a3f2c 40%,#3f2e22 70%,#2b241f 100%)" role="img" aria-label="Exterior of a custom home at sunset"></div>
    <div class="label">Lorem ipsum<svg width="14" height="10" viewBox="0 0 14 10"><path d="M0 5h12M8 1l4 4-4 4" stroke="#fff" stroke-width="1.6" fill="none"/></svg></div>
  </div>
  <div class="home-card" style="left:752px">
    <div class="photo" style="inset:0;background:radial-gradient(ellipse 60px 30px at 110px 110px,rgba(200,160,60,.5),rgba(200,160,60,0)),linear-gradient(180deg,#f1f1ef 0%,#e2e0dc 40%,#b8a48f 62%,#6e4b33 80%,#3a2a20 100%)" role="img" aria-label="White kitchen with wood island and pendant lights"></div>
    <div class="label">Lorem ipsum<svg width="14" height="10" viewBox="0 0 14 10"><path d="M0 5h12M8 1l4 4-4 4" stroke="#fff" stroke-width="1.6" fill="none"/></svg></div>
  </div>
  <div class="home-card" style="left:1027px;width:173px">
    <div class="photo" style="inset:0;background:radial-gradient(ellipse 70px 90px at 60px 110px,rgba(130,160,100,.6),rgba(130,160,100,0)),linear-gradient(180deg,#7a5a40 0%,#e6e4df 18%,#d8d6d0 60%,#b8aa96 80%,#6f6458 100%)" role="img" aria-label="Bright living room with tall windows"></div>
    <div class="label">Lorem ipsum</div>
  </div>
</section>

<section class="about">
  <div class="photo about-photo" role="img" aria-label="Family standing in front of their new home"></div>
  <div class="about-text">
    <h2 class="section-title">ABOUT US</h2>
    <div class="rule"></div>
    <p class="about-lead">Wade Holloran has been building stunning custom homes in the Indianapolis area for over 20 years.</p>
    <p class="about-body">As a small boutique building company we only build a handful of homes a year in order to offer our clients the personal attention that their homes deserve. It's this attention to detail that makes our client experience and final product something special and unique.</p>
    <div class="btn">Read More
      <svg width="16" height="10" viewBox="0 0 16 10"><path d="M0 5h14M10 1l4 4-4 4" stroke="#fff" stroke-width="1.6" fill="none"/></svg>
    </div>
  </div>
</section>

<section>
  <div class="builder-box">
    <div class="builder-text">
      <h2>HIGH END CUSTOM HOME BUILDER</h2>
      <p>Lorem ipsum dolor sit amet, consectetur adipiscing elit, sed do eiusmod tempor incididunt ut labore et dolore magna aliqua. Quis ipsum suspendisse ultrices gravida. Risus commodo viverra maecenas accumsan lacus vel facilisis.</p>
      <p>Quis ipsum suspendisse ultrices gravida. Risus commodo viverra maecenas accumsan lacus vel facilisis.</p>
    </div>
    <div class="btn">Read More
      <svg width="16" height="10" viewBox="0 0 16 10"><path d="M0 5h14M10 1l4 4-4 4" stroke="#fff" stroke-width="1.6" fill="none"/></svg>
    </div>
  </div>
  <div class="photo builder-photo" role="img" aria-label="Great room with stone fireplace and timber beams"></div>
</section>

<section class="quote-band">
  <p class="quote-text">“ Lorem ipsum dolor sit amet, consectetur adipiscing elit, sed do eiusmod tempor incididunt ut labore et dolore magna aliqua. Ut enim ad minim veniam, quis nostrud exercitation ullamco laboris nisi ut aliquip ex ea commodo consequat. Duis aute irure dolor in reprehenderit in voluptate velit esse cillum dolore eu fugiat nulla pariatur. ”</p>
  <div class="quote-author">- Marcus Dell</div>
</section>

<section>
  <div class="projects-title">
    <h2 class="section-title">PROJECTS</h2>
    <div class="rule"></div>
  </div>
  <div class="photo" style="left:38px;top:2962px;width:280px;height:291px;background:radial-gradient(ellipse 100px 40px at 140px 220px,rgba(240,238,234,.9),rgba(240,238,234,0)),linear-gradient(180deg,#f2f1ef 0%,#e0deda 30%,#8e8a85 55%,#a9a6a1 75%,#4a4642 100%)" role="img" aria-label="Living room with sectional sofa"></div>
  <div class="photo" style="left:334px;top:2962px;width:500px;height:291px;background:radial-gradient(ellipse 90px 40px at 250px 110px,rgba(80,130,70,.7),rgba(80,130,70,0)),linear-gradient(180deg,#e9e8e5 0%,#d2d0cc 18%,#4a3a30 38%,#6a5444 55%,#3a2b22 75%,#2a1f19 100%)" role="img" aria-label="Bar with stools and screens"></div>
  <div class="photo" style="left:849px;top:2962px;width:313px;height:291px;background:radial-gradient(ellipse 110px 60px at 160px 190px,rgba(255,255,255,.95),rgba(255,255,255,0)),linear-gradient(180deg,#d6d3ce 0%,#ebe9e6 40%,#dcd9d4 70%,#c9c5bf 100%)" role="img" aria-label="Bathroom with freestanding tub"></div>
  <div class="photo" style="left:38px;top:3276px;width:394px;height:292px;background:radial-gradient(ellipse 50px 90px at 197px 110px,rgba(255,255,255,.95),rgba(255,255,255,0)),linear-gradient(180deg,#dcdad6 0%,#eeedea 50%,#f4f3f1 70%,#8a7e72 85%,#4a403a 100%)" role="img" aria-label="Double vanity bathroom"></div>
  <div class="photo" style="left:452px;top:3276px;width:415px;height:292px;background:linear-gradient(180deg,#7e4622,#6f3d1d)" role="img" aria-label="Project photo with gallery overlay">
    <svg style="position:absolute;left:198px;top:136px" width="20" height="20" viewBox="0 0 20 20"><rect x="1" y="1" width="18" height="18" rx="4" fill="none" stroke="#fff" stroke-width="2"/><circle cx="10" cy="10" r="4" fill="none" stroke="#fff" stroke-width="2"/></svg>
  </div>
  <div class="photo" style="left:886px;top:3276px;width:276px;height:292px;background:radial-gradient(ellipse 70px 60px at 138px 130px,rgba(120,150,90,.55),rgba(120,150,90,0)),linear-gradient(180deg,#8a5a3a 0%,#a87650 14%,#ecebe8 30%,#e2e0dc 65%,#c7a984 82%,#a9835e 100%)" role="img" aria-label="Great room with timber ceiling"></div>
</section>

<section class="contact">
  <div class="photo office-photo" role="img" aria-label="Home office with desk and large window"></div>
  <div class="contact-text">
    <h2 class="section-title">CONTACT US</h2>
    <div class="rule"></div>
    <p class="intro">Lorem ipsum dolor sit amet, consectetur adipiscing elit, sed do eiusmod tempor incididunt ut labore et dolore magna aliqua. Quis ipsum suspendisse ultrices gravida. Risus commodo viverra maecenas. lacus vel facilisis.</p>
    <div class="contact-item">
      <div class="dot"><svg width="16" height="20" viewBox="0 0 16 20"><path d="M8 0C3.6 0 0 3.4 0 7.6 0 13 8 20 8 20s8-7 8-12.4C16 3.4 12.4 0 8 0z" fill="#fff"/><circle cx="8" cy="7.5" r="3" fill="#5e3212"/></svg></div>
      <div><h4>Location :</h4><span>415 North Fernmill Rd, Suite 308,<br>Carmel IN 46033</span></div>
    </div>
    <div class="contact-item">
      <div class="dot"><svg width="18" height="14" viewBox="0 0 18 14"><rect width="18" height="14" rx="2" fill="#fff"/><path d="M1 2l8 6 8-6" stroke="#5e3212" stroke-width="1.6" fill="none"/></svg></div>
      <div><h4>Email :</h4><span>wade@whcrafted.com</span></div>
    </div>
    <div class="contact-item">
      <div class="dot"><svg width="18" height="18" viewBox="0 0 24 24"><path d="M6.6 10.8c1.4 2.8 3.8 5.1 6.6 6.6l2.2-2.2c.3-.3.7-.4 1-.2 1.1.4 2.3.6 3.6.6.6 0 1 .4 1 1V20c0 .6-.4 1-1 1C10.6 21 3 13.4 3 4c0-.6.4-1 1-1h3.5c.6 0 1 .4 1 1 0 1.3.2 2.5.6 3.6.1.3 0 .7-.2 1z" fill="#fff"/></svg></div>
      <div><h4>Phone :</h4><span>317-552-7190</span></div>
    </div>
  </div>
</section>

<footer class="site-footer">
  <svg class="footer-shape" width="1200" height="371" viewBox="0 0 1200 371">
    <defs>
      <linearGradient id="footBand" x1="0" x2="1" y1="0" y2="0">
        <stop offset="0" stop-color="#5e3212"/><stop offset=".5" stop-color="#b05a1c"/><stop offset="1" stop-color="#5e3212"/>
      </linearGradient>
    </defs>
    <polygon points="0,90 600,0 1200,90 1200,371 0,371" fill="#2e2e2e"/>
    <polygon points="0,90 600,0 1200,90 1200,106 600,16 0,106" fill="url(#footBand)"/>
    <polygon points="0,106 600,16 1200,106 1200,118 600,30 0,118" fill="#ffffff"/>
    <polygon points="290,64 600,120 910,64 940,74 600,138 260,74" fill="url(#footBand)"/>
    <polygon points="260,74 600,138 940,74 960,80 600,146 240,80" fill="#ffffff"/>
  </svg>
  <div class="footer-brand">
    <div class="sq"></div>
    <div class="name">WADE HOLLORAN</div>
    <div class="sub">CUSTOM HOMES</div>
  </div>
  <nav class="footer-nav"><span>Home</span><span>|</span><span>About Us</span><span>|</span><span>Project</span><span>|</span><span>Contact Us</span></nav>
  <div class="footer-line"></div>
  <div class="copyright">Copyright © 2023 Wade Holloran Custom Homes | All Rights Reserved</div>
  <div class="social"><span></span><span></span><span></span></div>
</footer>

</body>
</html>
```